Dean Hollis Business Card

In addition to my name design (file uploaded), black print on white card stock, e-mail address should be presented as a typical e-mail address, i.e., underlined and in blue ink, the card should include the following information:
Professor of Aviation Technology
Accident Litigation Expert Witness
Master Certificated Flight Instructor

dhollis@vexmail.example
Anchorage, Alaska
(907) 318-5074

```html
<!DOCTYPE html>
<html lang="en">
<head>
<meta charset="utf-8">
<title>Dean Hollis Business Card</title>
<link rel="stylesheet" href="https://fonts.googleapis.com/css2?family=Archivo+Narrow:wght@400&family=Oswald:wght@500&display=swap">
<style>
  :root {
    --card-bg: #ffffff;
    --ink: #000000;
    --ink-muted: #56605f;
    --link-blue: #1a3de8;
    --art-fill: #0b0b0b;
  }
  html, body {
    margin: 0;
    padding: 0;
    overflow: hidden;
    background: var(--card-bg);
  }
  .card {
    position: relative;
    width: 1200px;
    height: 720px;
    background: var(--card-bg);
    overflow: hidden;
    color: var(--ink);
    font-family: "Archivo Narrow", "Arial Narrow", sans-serif;
  }
  .aircraft-art {
    position: absolute;
    left: 44px;
    top: 37px;
    width: 458px;
    height: 320px;
    background: var(--art-fill);
  }
  .name {
    position: absolute;
    left: 528px;
    top: 140px;
    margin: 0;
    font-family: "Oswald", "Arial Narrow", sans-serif;
    font-weight: 500;
    font-size: 84px;
    line-height: 1;
    letter-spacing: 2px;
    text-transform: uppercase;
    color: var(--ink);
  }
  .credentials {
    position: absolute;
    left: 526px;
    top: 290px;
    margin: 0;
    padding: 0;
    list-style: none;
    font-size: 29px;
    line-height: 38px;
    letter-spacing: 1px;
  }
  .credentials .secondary {
    color: var(--ink-muted);
  }
  .contact {
    position: absolute;
    left: 0;
    width: 1200px;
    top: 598px;
    margin: 0;
    text-align: center;
    font-size: 29px;
    letter-spacing: 1.5px;
    line-height: 1;
  }
  .contact a {
    color: var(--link-blue);
    text-decoration: underline;
  }
  .contact .sep {
    margin: 0 24px;
  }
</style>
</head>
<body>
  <div class="card">
    <div class="aircraft-art" role="img" aria-label="Black silhouette of a jet airliner seen from above, flying right"></div>
    <h1 class="name">Dean E. Hollis</h1>
    <ul class="credentials">
      <li>Professor of Aviation Technology</li>
      <li class="secondary">Accident Litigation&nbsp; Expert Witness</li>
      <li>Master Certificated Flight Instructor</li>
    </ul>
    <p class="contact">
      <a href="mailto:dhollis@vexmail.example">dhollis@vexmail.example</a><span class="sep">|</span>Anchorage, Alaska<span class="sep">|</span>(907) 318-5074
    </p>
  </div>
</body>
</html>
```